Webdesign/ Redesign of community frontpage (only design, no code!)

Our social community website (http://www.tavro.eu) needs a fresh, more invitating frontpage. Our audience are 14 - 25 year old.

Only the screen design (psd & image) is needed, no code (no html, no css, ...).

Style:
- Modern/ clear/ lightweight/ invitating design for young people
- Emphasize the intent of the website (social community website, meeting other young people to chat, hangout, ..)
- Optimized for 1024x768

Elements that must appear:
- Logo (attached as EPS, can be modified if needed)
- Login form (Username, Password, Status/Feeling, Forgot password link, ...)
- Link to registration page OR registration form
- Empty space (around 350x250 pixel) where a video or other dynamic content could be embedded (done by myself)
- Five feature/pro statements (max. 60 letters each, not necessarily to be displayed as a group, see below)
- Currently present links in footer
- Some statistics (Number of people online, total number of members (females/ males))

Elements that might appear:
- Registration form instead of link to separate registration form (ex like chatterloop has it)

Ideas:
- Registration form could also be designed to be a layer that'll show when the user clicks
- If the design needs/allows it, I can also animate random member photos (80x80 pixels) and place them on the frontpage using js/ ajax

Feature/pro statements examples (see above):
- Dauerhaft kostenlos für Frauen und Männer
- Reale Profile, extrem wenig Fakes & Störenfriede
- Persönliches Profil mit vielen Funktionen
- Hoher Schutz deiner Privatsphäre und Daten
- Viele freundliche Mitarbeiter und Helfer
Updates

After having reviewed the first two designs, I'd like to give these general ideas/ feedback:

1. I think it would be much better to _not_ have the whole registration form on the frontpage but instead only a link which opens the form in a layer/dialog when clicked. Of course only the design of the dialog needs to be done, I'll do the actual coding. To have a first impression of how the dialog could look like, please see the newly attached dialog.png (the text in the dialog is just for demo and should be replaced by the actual registration form).

2. There should be no separation between males/ females like it is currently. I think it'd better to mix because it emphasizes the community/ group character of the site and does not make it look too much like da dating site.

3. I think the five statements/ pros I mentioned (why should people register, what are the greatest features of our site, ..) could be best displayed as balloon tips (just like in comics) next to some images of users.

4. The color of the site should not be too heavy and should make people feel comfortable.

5. The logo provied must be fixed to read "TAVRO.eu" instead of "LUNEK.de". I hope this i no big deal, sorry for that. This could also be done afterwards for a small additional amount of money, as it doesn't really affect the overall design.

To better illustrate all my writings above I just made two simple sketches and attached them (frontpage.png and frontpage_with_active_registration.png).

Important: these only show all the elements that must appear on the page and what I thought might be a good idea of how to present the pros/ features of my site. The actual placements, sizes, arragements etc. can of course all be different.

Looking forward to your create additions and design skills to make this look pretty... :-)

Just to emphasize, the design should not look or feel heavy. So please keep the colors light/ soft, no huge images, don't stretch the logo to much, etc.

Please do not insert any content (like search boxes, text blocks, etc.) which is not already present in my mockups. The only thing that should be additionally added is a link/ button so people can login using openid (chatterloop, wexplore, ..) too.

Target Market(s)

Young people 14 - 25 years old interested in meeting friends, new people, chat, flirt, hangout, have fun.

Industry/Entity Type

Community

Requirements
Must have
• see description
Nice to have
• see description
Should not have
• plugin dependencies (ex flash)

```html
<!DOCTYPE html>
<html lang="en">
<head>
<meta charset="utf-8">
<title>TAVRO.eu – chat, flirt &amp; more</title>
<link rel="stylesheet" href="https://fonts.googleapis.com/css2?family=Source+Sans+3:wght@400;600;700&display=swap">
<style>
  :root {
    --page-bg: #dcdcf1;
    --panel-bg: #ffffff;
    --panel-tint: #d6d2f3;
    --header-top: #8b82dc;
    --header-bottom: #5b50b6;
    --frame: #6f66c6;
    --frame-dark: #4f4699;
    --text-dark: #444444;
    --text-light: #ffffff;
    --link-light: #a9e6ff;
    --stat-text: #4b4196;
    --field-bg: #ffffff;
    --field-line: #cfcbea;
    --slot-text: #8a8a8a;
  }
  * { box-sizing: border-box; margin: 0; padding: 0; }
  html, body { width: 1200px; height: 900px; overflow: hidden; }
  body {
    position: relative;
    background: var(--page-bg);
    font-family: "Source Sans 3", Arial, sans-serif;
    color: var(--text-dark);
  }

  .site-panel {
    position: absolute;
    left: 64px; top: 47px;
    width: 1073px; height: 811px;
    border: 2px solid var(--frame);
    border-radius: 10px;
    background:
      radial-gradient(ellipse 520px 520px at 95% 85%, var(--panel-tint), rgba(214,210,243,0) 70%),
      var(--panel-bg);
    overflow: hidden;
  }

  .site-header {
    position: absolute; left: 0; top: 0;
    width: 100%; height: 172px;
    background: linear-gradient(180deg, var(--header-top), var(--header-bottom));
    color: var(--text-light);
    box-shadow: 0 3px 6px rgba(60,50,130,0.35);
    z-index: 5;
  }
  .brand { position: absolute; left: 26px; top: 18px; }
  .brand-name {
    display: flex; align-items: center; gap: 12px;
    font-size: 56px; font-weight: 700; line-height: 1; letter-spacing: 2px;
  }
  .brand-mark { width: 40px; height: 40px; background: var(--text-light); border-radius: 50%; }
  .brand-tagline { margin-top: 6px; font-size: 31px; font-weight: 700; letter-spacing: 3px; }
  .brand-intro { position: absolute; left: 26px; top: 136px; font-size: 19px; }

  .signup-prompt { position: absolute; left: 380px; top: 62px; width: 340px; text-align: center; }
  .signup-question { font-size: 23px; }
  .signup-link {
    display: block; margin-top: 4px;
    font-size: 18px; white-space: nowrap;
    color: var(--link-light); text-decoration: underline;
  }

  .login-form { position: absolute; left: 737px; top: 20px; width: 330px; height: 150px; }
  .field-label { position: absolute; font-size: 15px; font-weight: 600; }
  .text-field {
    position: absolute; width: 151px; height: 28px;
    background: var(--field-bg); border: 1px solid var(--field-line);
  }
  .status-select {
    position: absolute; left: 172px; top: 22px; width: 149px; height: 28px;
    background: var(--field-bg); color: var(--text-dark);
    font-size: 16px; padding: 4px 0 0 11px;
  }
  .status-arrow {
    position: absolute; right: 0; top: 0; width: 28px; height: 28px;
    background: var(--frame-dark);
  }
  .login-button {
    position: absolute; left: 172px; top: 79px; width: 149px; height: 29px;
    background: var(--field-bg); color: var(--text-dark);
    font-size: 16px; padding: 4px 0 0 11px;
  }
  .remember {
    position: absolute; left: 0; top: 113px;
    display: flex; align-items: center; gap: 6px; font-size: 15px;
  }
  .remember-box { width: 20px; height: 20px; background: var(--field-bg); }
  .forgot-link {
    position: absolute; left: 172px; top: 115px;
    font-size: 15px; color: var(--link-light); text-decoration: none;
  }

  .member-photo {
    position: absolute; width: 96px; height: 96px;
    border: 2px solid var(--frame); border-radius: 4px;
  }
  .tone-a { background: linear-gradient(160deg, #6b5a55, #c9a79a); }
  .tone-b { background: linear-gradient(160deg, #b8a393, #e7d8cc); }
  .tone-c { background: linear-gradient(160deg, #3a2f2e, #8c6f63); }
  .tone-d { background: linear-gradient(160deg, #a9b8b0, #d8cbc4); }
  .tone-e { background: linear-gradient(160deg, #2a2628, #6e5a52); }
  .tone-f { background: linear-gradient(160deg, #c04f55, #3b2b2c); }
  .tone-g { background: linear-gradient(160deg, #74a8c2, #d7c6b8); }
  .tone-h { background: linear-gradient(160deg, #e0e0dc, #7d6d66); }

  .speech-bubble { position: absolute; width: 325px; height: 87px; z-index: 3; }
  .speech-bubble svg { position: absolute; left: 0; top: 0; }
  .bubble-text {
    position: absolute; left: 12px; top: 0; width: 311px; height: 59px;
    font-size: 13px; line-height: 17px; padding: 12px 16px 0 30px;
  }
  .bubble-author { display: block; text-align: right; padding-right: 20px; }
  .bubble-author.inline { margin-top: -17px; }

  .media-slot {
    position: absolute; left: 722px; top: 504px;
    width: 303px; height: 227px;
    background: var(--panel-bg);
    border: 2px solid var(--frame); border-radius: 8px;
    display: flex; align-items: center; justify-content: center;
    font-size: 42px; color: var(--slot-text);
  }

  .site-stats { position: absolute; left: 36px; top: 744px; color: var(--stat-text); font-size: 20px; line-height: 26px; }
  .site-stats .online { padding-left: 9px; }

  .site-footer {
    position: absolute; left: 76px; top: 863px;
    font-size: 14px; color: var(--text-light); word-spacing: 2px;
  }
</style>
</head>
<body>
  <main class="site-panel">
    <header class="site-header">
      <div class="brand">
        <div class="brand-name"><span class="brand-mark"></span>TAVRO.eu</div>
        <div class="brand-tagline">chat, flirt &amp; more</div>
      </div>
      <p class="brand-intro">TAVRO helps you connect and share with the people in your life.</p>

      <div class="signup-prompt">
        <p class="signup-question">No account yet?</p>
        <a class="signup-link" href="#">Sign up - it's free and always will be!</a>
      </div>

      <form class="login-form">
        <span class="field-label" style="left:0;top:0">User Name</span>
        <span class="text-field" style="left:0;top:22px"></span>
        <span class="field-label" style="left:0;top:57px">Password</span>
        <span class="text-field" style="left:0;top:79px"></span>
        <span class="status-select">Status/Feeling
          <span class="status-arrow">
            <svg width="28" height="28" viewBox="0 0 28 28"><path d="M7 10 H21 L14 20 Z" fill="#ffffff"/></svg>
          </span>
        </span>
        <span class="login-button">Log in</span>
        <label class="remember"><span class="remember-box"></span>Remeber me</label>
        <a class="forgot-link" href="#">Forgot password?</a>
      </form>
    </header>

    <div class="member-photo tone-a" style="left:56px;top:236px" role="img" aria-label="Member photo"></div>
    <div class="member-photo tone-b" style="left:279px;top:274px" role="img" aria-label="Member photo"></div>
    <div class="member-photo tone-c" style="left:97px;top:361px" role="img" aria-label="Member photo"></div>
    <div class="member-photo tone-d" style="left:395px;top:359px" role="img" aria-label="Member photo"></div>
    <div class="member-photo tone-c" style="left:242px;top:402px" role="img" aria-label="Member photo"></div>
    <div class="member-photo tone-f" style="left:723px;top:195px" role="img" aria-label="Member photo"></div>
    <div class="member-photo tone-b" style="left:518px;top:313px" role="img" aria-label="Member photo"></div>
    <div class="member-photo tone-g" style="left:936px;top:269px" role="img" aria-label="Member photo"></div>
    <div class="member-photo tone-h" style="left:706px;top:324px" role="img" aria-label="Member photo"></div>
    <div class="member-photo tone-e" style="left:547px;top:416px" role="img" aria-label="Member photo"></div>
    <div class="member-photo tone-d" style="left:852px;top:386px" role="img" aria-label="Member photo"></div>
    <div class="member-photo tone-g" style="left:47px;top:558px" role="img" aria-label="Member photo"></div>
    <div class="member-photo tone-e" style="left:378px;top:537px" role="img" aria-label="Member photo"></div>
    <div class="member-photo tone-a" style="left:570px;top:526px" role="img" aria-label="Member photo"></div>
    <div class="member-photo tone-b" style="left:187px;top:631px" role="img" aria-label="Member photo"></div>
    <div class="member-photo tone-h" style="left:309px;top:692px" role="img" aria-label="Member photo"></div>
    <div class="member-photo tone-d" style="left:490px;top:668px" role="img" aria-label="Member photo"></div>

    <div class="speech-bubble" style="left:150px;top:206px">
      <svg width="325" height="87" viewBox="0 0 325 87">
        <defs><linearGradient id="bubbleFill" x1="0" y1="0" x2="0" y2="1"><stop offset="0" stop-color="#ffffff"/><stop offset="1" stop-color="#e6e2f6"/></linearGradient></defs>
        <path d="M22 1 H313 Q323 1 323 11 V49 Q323 59 313 59 H36 L5 85 L13 41 V11 Q13 1 22 1 Z" fill="url(#bubbleFill)" stroke="#6f66c6" stroke-width="1.5"/>
      </svg>
      <p class="bubble-text">I like it because it;s free for everyone!<span class="bubble-author">Mila 16,&nbsp;&nbsp; aus 93 Kelheim</span></p>
    </div>
    <div class="speech-bubble" style="left:610px;top:252px">
      <svg width="325" height="87" viewBox="0 0 325 87"><path d="M22 1 H313 Q323 1 323 11 V49 Q323 59 313 59 H36 L5 85 L13 41 V11 Q13 1 22 1 Z" fill="url(#bubbleFill)" stroke="#6f66c6" stroke-width="1.5"/></svg>
      <p class="bubble-text">It's great to hang out, chat and make new friends!<span class="bubble-author inline">NightOwlSky 20m,</span></p>
    </div>
    <div class="speech-bubble" style="left:141px;top:491px">
      <svg width="325" height="87" viewBox="0 0 325 87"><path d="M22 1 H313 Q323 1 323 11 V49 Q323 59 313 59 H36 L5 85 L13 41 V11 Q13 1 22 1 Z" fill="url(#bubbleFill)" stroke="#6f66c6" stroke-width="1.5"/></svg>
      <p class="bubble-text">It's great to hang out, chat and make new friends!<span class="bubble-author inline">NightOwlSky 20m,</span></p>
    </div>
    <div class="speech-bubble" style="left:279px;top:596px">
      <svg width="325" height="87" viewBox="0 0 325 87"><path d="M22 1 H313 Q323 1 323 11 V49 Q323 59 313 59 H36 L5 85 L13 41 V11 Q13 1 22 1 Z" fill="url(#bubbleFill)" stroke="#6f66c6" stroke-width="1.5"/></svg>
      <p class="bubble-text">I like it because it;s free for everyone!<span class="bubble-author">Mila 16,&nbsp;&nbsp; aus 93 Kelheim</span></p>
    </div>

    <div class="media-slot">Image</div>

    <div class="site-stats">
      <p>89,433&nbsp; Members</p>
      <p class="online">4,645&nbsp; online now</p>
    </div>
  </main>

  <footer class="site-footer">I&nbsp; Foot Note&nbsp; I&nbsp; Foot Note&nbsp; I&nbsp; Foot Note&nbsp; I&nbsp; Foot Note&nbsp; I</footer>
</body>
</html>
```